Website of QUORVEX | The Amber Frontier Company

I need a simple and effective website where users can quickly understand what the company is all about and the added value of the services provided. The site should be attractive and modern, based on the logo and on the corporate slideshow attached.

Target Market(s)

Public and Private organizations from maritime security and defense, looking for solutions in the field s of digital transformation and cybersecurity.

Coding

Coded - Design and coding required

Requirements
Must have
• A form through which can contact the company by email to request additional information.

```html
<!DOCTYPE html>
<html lang="en">
<head>
<meta charset="utf-8">
<title>QUORVEX | The Amber Frontier Company</title>
<link href="https://fonts.googleapis.com/css2?family=Montserrat:wght@500;600;700;800&family=Lato:wght@400;700;900&display=swap" rel="stylesheet">
<style>
:root{
  --blue:#3a95d5;
  --blue-deep:#1f6fb8;
  --ink:#0b0b0b;
  --navy-card:#15293a;
  --white:#ffffff;
  --text:#222222;
  --field-border:#b9c2cc;
}
*{margin:0;padding:0;box-sizing:border-box}
html,body{width:1200px;height:4161px;overflow:hidden;background:var(--white)}
body{position:relative;font-family:'Lato',sans-serif;color:var(--text)}
.section{position:absolute;left:0;width:1200px}
h1,h2,h3{font-family:'Montserrat',sans-serif}

/* buttons */
.btn{position:absolute;display:flex;align-items:center;justify-content:space-between;border:2px solid #1a1a1a;border-radius:40px;padding:0 4px 0 26px;font-family:'Lato',sans-serif;font-weight:900;font-size:15px;color:#111;text-decoration:none;background:transparent;cursor:pointer}
.btn .arrow{width:36px;height:36px;border-radius:50%;background:var(--blue-deep);display:flex;align-items:center;justify-content:center}
.btn.light{border-color:#fff;color:#fff}

/* header */
.site-header{top:0;height:84px;z-index:10;background:#fff}
.brand{position:absolute;left:100px;top:22px;display:flex;align-items:center;gap:10px}
.brand .mark{width:36px;height:36px;background:var(--blue);border-radius:4px}
.brand .name{font-family:'Montserrat',sans-serif;font-weight:700;font-size:28px;line-height:1;color:#111;letter-spacing:.5px}
.brand .sub{font-family:'Montserrat',sans-serif;font-weight:700;font-size:9px;letter-spacing:3.5px;color:#111;margin-top:3px}
.main-nav{position:absolute;left:518px;top:33px}
.main-nav a{font-size:15px;color:#555;text-decoration:none;position:absolute;white-space:nowrap}
.main-nav a.active{color:#111;font-weight:700}

/* hero */
.hero{top:84px;height:676px;z-index:1;background:linear-gradient(120deg,#1a3550 0%,#2e5774 40%,#5d7f98 70%,#8aa3b6 100%);border-bottom-right-radius:150px;overflow:hidden}
.hero .photo{position:absolute;inset:0;background:radial-gradient(ellipse at 78% 55%,rgba(60,70,85,.85) 0%,rgba(40,60,80,.4) 25%,transparent 45%)}
.hero h1{position:absolute;left:100px;top:68px;font-weight:800;font-size:44px;line-height:51px;color:#fff;text-transform:uppercase;width:640px}
.hero .lead{position:absolute;left:100px;top:232px;font-family:'Montserrat',sans-serif;font-weight:600;font-size:27px;line-height:39px;color:#fff;width:580px}
.hero .tagline{position:absolute;left:100px;top:326px;font-family:'Montserrat',sans-serif;font-weight:500;font-size:22px;color:#fff}

/* about */
.about{top:617px;height:760px;z-index:2;background:#fff;border-top-left-radius:150px}
.about .visual{position:absolute;left:100px;top:115px;width:465px;height:471px;border-radius:18px 48% 48% 48%/18px 30% 30% 30%;background:linear-gradient(135deg,#d7dde2,#9eb0bd 50%,#3f5a4d)}
.about h2{position:absolute;left:712px;top:166px;font-size:48px;font-weight:800;color:#111}
.rule{position:absolute;height:3px;width:97px;background:var(--blue-deep)}
.about .rule{left:712px;top:228px}
.about .copy{position:absolute;left:712px;top:272px;width:380px;font-size:15.5px;line-height:26px;color:#333}
.about .copy p+p{margin-top:9px}
.about .btn{left:712px;top:471px;width:166px;height:44px}

/* strategy */
.strategy{top:1297px;height:680px;z-index:3;background:var(--blue);border-top-right-radius:110px;color:#fff}
.eyebrow{font-family:'Montserrat',sans-serif;font-weight:500;font-size:15px;text-transform:uppercase}
.strategy .eyebrow{position:absolute;left:100px;top:151px}
.strategy h2{position:absolute;left:100px;top:178px;font-size:48px;font-weight:800;line-height:51px}
.strategy .rule{left:100px;top:299px;background:#fff}
.strategy .intro{position:absolute;left:100px;top:331px;width:420px;font-size:15.5px;line-height:26px}
.svc{position:absolute;color:#fff}
.svc svg{display:block}
.svc h3{font-weight:500;font-size:21px;line-height:25px}
.svc p{font-family:'Montserrat',sans-serif;font-size:15px;line-height:25px;margin-top:12px}
.divider-v{position:absolute;left:825px;top:68px;width:2px;height:247px;background:rgba(255,255,255,.45)}
.divider-h{position:absolute;left:568px;top:316px;width:530px;height:2px;background:rgba(255,255,255,.45)}

/* execution */
.execution{top:1836px;height:914px;z-index:4;background:var(--ink);border-top-left-radius:130px;color:#fff}
.execution .eyebrow{position:absolute;left:100px;top:115px;color:var(--blue)}
.execution h2{position:absolute;left:100px;top:138px;font-size:48px;font-weight:800;line-height:51px}
.execution .rule{left:100px;top:255px}
.execution .intro{position:absolute;left:594px;top:144px;width:480px;font-size:15.5px;line-height:26px}
.card{position:absolute;width:480px;height:153px;background:var(--navy-card)}
.card .corner{position:absolute;width:26px;height:26px;border:0 solid #fff}
.card .tl{left:0;top:0;border-left-width:3px;border-top-width:3px}
.card .tr{right:0;top:0;border-right-width:3px;border-top-width:3px}
.card .bl{left:0;bottom:0;border-left-width:3px;border-bottom-width:3px}
.card .br{right:0;bottom:0;border-right-width:3px;border-bottom-width:3px}
.card svg{position:absolute;left:26px;top:40px}
.card h3{position:absolute;left:142px;top:33px;font-weight:600;font-size:21px}
.card p{position:absolute;left:142px;top:72px;width:300px;font-family:'Montserrat',sans-serif;font-size:15px;line-height:25px}

/* why */
.why{top:2613px;height:800px;z-index:5;background:#fff;border-top-right-radius:130px}
.why h2{position:absolute;left:0;width:1200px;text-align:center;top:95px;font-size:48px;font-weight:800;color:#111}
.why .rule{left:551px;top:168px}
.reasons{position:absolute;left:100px;top:268px;width:550px;list-style:none}
.reasons li{position:relative;padding-left:38px;margin-bottom:16px;font-size:15.5px;line-height:26px;color:#333}
.reasons li b{display:block;color:#111;font-weight:900}
.reasons li svg{position:absolute;left:0;top:4px}
.why .visual{position:absolute;left:686px;top:257px;width:415px;height:397px;border-radius:24px 48% 48% 24px/24px 30% 30% 24px;background:linear-gradient(160deg,#2f6fae,#1c4f86 55%,#123a66)}

/* collaborate */
.collab{top:3300px;height:560px;z-index:6;background:#fff}
.collab .network{position:absolute;left:0;top:318px;width:1200px;height:180px;background:linear-gradient(180deg,rgba(255,255,255,0),#f1f2f4 60%,#e9ebee)}
.collab h2{position:absolute;left:0;width:1200px;text-align:center;top:98px;font-size:48px;font-weight:800;color:#111}
.collab .rule{left:551px;top:174px}
.collab h3{position:absolute;left:0;width:1200px;text-align:center;top:222px;font-family:'Lato',sans-serif;font-weight:900;font-size:22px;color:#111}
.collab .pitch{position:absolute;left:300px;width:600px;text-align:center;top:278px;font-size:15.5px;line-height:26px;color:#333}
.contact-form{position:absolute;left:0;top:347px;width:1200px;height:44px}
.contact-form .field{position:absolute;top:0;height:44px;border:1.5px solid var(--field-border);border-radius:40px;background:#fff;padding:0 20px;font-family:'Lato',sans-serif;font-size:15px;color:#111}
.contact-form .field::placeholder{color:#777}
.contact-form .email{left:215px;width:280px}
.contact-form .message{left:510px;width:290px}
.contact-form .btn{left:815px;top:0;width:166px;height:44px;background:#fff}

/* footer */
.site-footer{top:3798px;height:363px;z-index:7;background:var(--ink);border-top-left-radius:100px;color:#fff}
.site-footer .brand{left:100px;top:92px}
.site-footer .brand .mark{width:56px;height:56px;border-radius:6px}
.site-footer .brand .name{color:#fff;font-size:42px}
.site-footer .brand .sub{color:#fff;font-size:13px;letter-spacing:5.5px}
.contact{position:absolute;display:flex;align-items:center;gap:22px;top:101px}
.contact .ic{width:59px;height:59px;border-radius:50%;background:var(--blue-deep);display:flex;align-items:center;justify-content:center}
.contact small{display:block;font-size:15px}
.contact strong{display:block;font-size:19px;font-weight:900;margin-top:2px}
.site-footer .line{position:absolute;left:100px;top:207px;width:1000px;height:1px;background:#444}
.footer-nav{position:absolute;left:0;width:1200px;top:250px;display:flex;justify-content:center;gap:38px}
.footer-nav a{color:#fff;text-decoration:none;font-size:15.5px}
.copyright{position:absolute;left:0;width:1200px;top:294px;text-align:center;font-size:15.5px}
</style>
</head>
<body>

<header class="section site-header">
  <div class="brand">
    <span class="mark"></span>
    <div><div class="name">QUORVEX</div><div class="sub">AMBER FRONTIER</div></div>
  </div>
  <nav class="main-nav">
    <a class="active" href="#" style="left:0">Home</a>
    <a href="#" style="left:78px">About</a>
    <a href="#" style="left:157px">Services</a>
    <a href="#" style="left:250px">News</a>
    <a href="#" style="left:325px">Contact</a>
  </nav>
  <a class="btn" href="#contact" style="left:934px;top:22px;width:165px;height:44px">Get Started
    <span class="arrow"><svg width="16" height="16" viewBox="0 0 16 16"><path d="M2 8h11M9 4l4 4-4 4" stroke="#fff" stroke-width="1.8" fill="none" stroke-linecap="round"/></svg></span></a>
</header>

<section class="section hero">
  <div class="photo" role="img" aria-label="Patrol vessel cutting through open sea with a faint digital security overlay"></div>
  <h1>Innovative solutions for maritime security and defense</h1>
  <p class="lead">Empowering organizations with cutting-edge consulting and technology</p>
  <p class="tagline">Where Innovation Meets Fulfillment</p>
  <a class="btn light" href="#contact" style="left:100px;top:386px;width:166px;height:44px">Get Started
    <span class="arrow"><svg width="16" height="16" viewBox="0 0 16 16"><path d="M2 8h11M9 4l4 4-4 4" stroke="#fff" stroke-width="1.8" fill="none" stroke-linecap="round"/></svg></span></a>
</section>

<section class="section about">
  <div class="visual" role="img" aria-label="Two colleagues working together at a desktop computer in an office"></div>
  <h2>ABOUT US</h2>
  <span class="rule"></span>
  <div class="copy">
    <p><b>QUORVEX</b> specializes in delivering innovative solutions for maritime security and defense in the fields of digital transformation and cybersecurity.</p>
    <p>By combining unparalleled expertise with strategic partnerships, we empower organizations to overcome challenges, seize opportunities, and achieve success.</p>
  </div>
  <a class="btn" href="#">Learn More
    <span class="arrow"><svg width="16" height="16" viewBox="0 0 16 16"><path d="M2 8h11M9 4l4 4-4 4" stroke="#fff" stroke-width="1.8" fill="none" stroke-linecap="round"/></svg></span></a>
</section>

<section class="section strategy">
  <p class="eyebrow">Our Services</p>
  <h2>STRATEGY AND<br>DESIGN</h2>
  <span class="rule"></span>
  <p class="intro">Services focused on helping clients define their vision, assess their needs, and design innovative solutions, including:</p>

  <div class="divider-v"></div>
  <div class="divider-h"></div>

  <div class="svc" style="left:594px;top:73px;width:220px">
    <svg width="68" height="68" viewBox="0 0 68 68" fill="none" stroke="#111" stroke-width="2"><rect x="4" y="4" width="38" height="50" rx="2"/><path d="M11 16h5l2 3 4-6M26 16h10M11 28h5l2 3 4-6M26 28h10M11 40h20"/><circle cx="50" cy="44" r="11"/><path d="M45 44l4 4 7-7M44 54l-3 10 9-4 9 4-3-10"/></svg>
    <h3 style="margin-top:12px">Strategic<br>Assessments</h3>
    <p>Conducting market surveys, identifying challenges, and uncovering opportunities.</p>
  </div>
  <div class="svc" style="left:862px;top:73px;width:230px">
    <svg width="68" height="68" viewBox="0 0 68 68" fill="none" stroke="#111" stroke-width="2"><circle cx="34" cy="28" r="16"/><path d="M27 28l5 5 9-10M27 48h14M28 54h12M31 60h6M34 4v4M12 28H8M60 28h-4M17 11l3 3M51 11l-3 3"/></svg>
    <h3 style="margin-top:12px">Solution<br>Design</h3>
    <p>Crafting tailored, innovative, and feasible solutions.</p>
  </div>
  <div class="svc" style="left:594px;top:358px;width:70px">
    <svg width="68" height="68" viewBox="0 0 68 68" fill="none" stroke="#111" stroke-width="2"><circle cx="56" cy="12" r="8"/><circle cx="56" cy="12" r="3"/><circle cx="12" cy="46" r="7"/><circle cx="12" cy="46" r="2.5"/><path d="M56 20v6c0 6-4 8-10 8H30c-6 0-6 10 0 10h8c6 0 6 12 0 12H18"/></svg>
  </div>
  <div class="svc" style="left:694px;top:350px;width:400px">
    <h3>Strategic<br>Roadmaps</h3>
    <p>Developing high-level plans that outline the steps, priorities, and resources needed to achieve the organization's vision.</p>
  </div>
</section>

<section class="section execution">
  <p class="eyebrow">Our Services</p>
  <h2>EXECUTION AND<br>DELIVERY</h2>
  <span class="rule"></span>
  <p class="intro">Services focused on turning strategies into reality by driving implementation, integration, and operational success, including:</p>

  <div class="card" style="left:103px;top:333px">
    <span class="corner tl"></span><span class="corner tr"></span><span class="corner bl"></span><span class="corner br"></span>
    <svg width="78" height="78" viewBox="0 0 78 78" fill="none" stroke="#fff" stroke-width="2"><circle cx="39" cy="39" r="35"/><circle cx="39" cy="39" r="22"/><circle cx="39" cy="39" r="13"/><path d="M42 33c-1-2-6-2-6 1s6 2 6 5-5 3-6 1M39 30v18"/></svg>
    <h3>Funding Assistance</h3>
    <p>Identifying funding opportunities and designing proposals.</p>
  </div>
  <div class="card" style="left:607px;top:333px">
    <span class="corner tl"></span><span class="corner tr"></span><span class="corner bl"></span><span class="corner br"></span>
    <svg width="80" height="78" viewBox="0 0 80 78" fill="none" stroke="#fff" stroke-width="2"><path d="M4 34l14-10 12 4 10-4 12 4 14-6 10 12-10 14-8 8-8 4-10-4-10-6-12-6zM30 28l14 10M40 2v10M26 6l4 8M54 6l-4 8"/></svg>
    <h3>Partnership Development</h3>
    <p>Identifying and aligning strategic partners for joint developments.</p>
  </div>
  <div class="card" style="left:103px;top:514px">
    <span class="corner tl"></span><span class="corner tr"></span><span class="corner bl"></span><span class="corner br"></span>
    <svg width="80" height="80" viewBox="0 0 80 80" fill="none" stroke="#fff" stroke-width="2"><circle cx="16" cy="14" r="7"/><circle cx="30" cy="22" r="7"/><circle cx="14" cy="30" r="7"/><path d="M44 34l12-12 12 12c10 10 8 32-10 36-14 4-24-4-26-12l12-12c2 8 10 10 14 6s2-10-4-12z"/></svg>
    <h3>Acquisition Support</h3>
    <p>Defining requirements and assessing offers to ensure the best fit.</p>
  </div>
  <div class="card" style="left:607px;top:514px">
    <span class="corner tl"></span><span class="corner tr"></span><span class="corner bl"></span><span class="corner br"></span>
    <svg width="80" height="78" viewBox="0 0 80 78" fill="none" stroke="#fff" stroke-width="2"><rect x="4" y="4" width="50" height="66" rx="2"/><path d="M12 16h8v8h-8zM12 34h8v8h-8zM12 52h8v8h-8zM26 20h18M26 38h10"/><rect x="38" y="40" width="38" height="32" rx="2"/><path d="M38 50h38M46 36v8M68 36v8M45 56h6v5h-6zM56 56h6v5h-6zM67 56h4v5h-4z"/></svg>
    <h3>Project management</h3>
    <p>Delivering projects on schedule and within budget while ensuring quality.</p>
  </div>
</section>

<section class="section why">
  <h2>WHY CHOOSE US</h2>
  <span class="rule"></span>
  <ul class="reasons">
    <li><svg width="20" height="20" viewBox="0 0 20 20"><circle cx="10" cy="10" r="10" fill="#1f6fb8"/><path d="M5.5 10l3 3 6-6" stroke="#fff" stroke-width="2" fill="none"/></svg><b>Expert Team</b>Decades of combined worldwide experience in maritime security, defense, digital transformation, and cybersecurity, in public, private and research organizations, and in multinational and multidisciplinary teams.</li>
    <li><svg width="20" height="20" viewBox="0 0 20 20"><circle cx="10" cy="10" r="10" fill="#1f6fb8"/><path d="M5.5 10l3 3 6-6" stroke="#fff" stroke-width="2" fill="none"/></svg><b>Proven Partnerships</b>Access to state-of-the-art knowledge, practices and technology through key alliances.</li>
    <li><svg width="20" height="20" viewBox="0 0 20 20"><circle cx="10" cy="10" r="10" fill="#1f6fb8"/><path d="M5.5 10l3 3 6-6" stroke="#fff" stroke-width="2" fill="none"/></svg><b>Tailored Strategies</b>Customized designs addressing unique organizational needs.</li>
    <li><svg width="20" height="20" viewBox="0 0 20 20"><circle cx="10" cy="10" r="10" fill="#1f6fb8"/><path d="M5.5 10l3 3 6-6" stroke="#fff" stroke-width="2" fill="none"/></svg><b>Innovative Solutions</b>Leveraging cutting-edge technology and strategic insights.</li>
  </ul>
  <div class="visual" role="img" aria-label="Container ship sailing across deep blue ocean seen from above"></div>
</section>

<section class="section collab" id="contact">
  <div class="network" role="img" aria-label="Soft grey connected-network pattern fading into the page"></div>
  <h2>LET'S COLLABORATE</h2>
  <span class="rule"></span>
  <h3>Ready to innovate together?</h3>
  <p class="pitch"><b>QUORVEX</b> is here to help you navigate challenges and unlock new opportunities for maritime security and defense with digital transformation and cybersecurity solutions.</p>
  <form class="contact-form" action="mailto:office@quorvex.com" method="post" enctype="text/plain">
    <input class="field email" type="email" name="email" placeholder="Your email" aria-label="Your email" required>
    <input class="field message" type="text" name="message" placeholder="How can we help?" aria-label="Your message" required>
    <button class="btn" type="submit">Contact Us
      <span class="arrow"><svg width="16" height="16" viewBox="0 0 16 16"><path d="M2 8h11M9 4l4 4-4 4" stroke="#fff" stroke-width="1.8" fill="none" stroke-linecap="round"/></svg></span></button>
  </form>
</section>

<footer class="section site-footer">
  <div class="brand">
    <span class="mark"></span>
    <div><div class="name">QUORVEX</div><div class="sub">AMBER FRONTIER</div></div>
  </div>
  <div class="contact" style="left:568px">
    <span class="ic"><svg width="26" height="20" viewBox="0 0 26 20"><rect x="1" y="1" width="24" height="18" rx="2" fill="#fff"/><path d="M2 3l11 8 11-8" stroke="#1f6fb8" stroke-width="2" fill="none"/></svg></span>
    <div><small>Email Us</small><strong>office@quorvex.com</strong></div>
  </div>
  <div class="contact" style="left:875px">
    <span class="ic"><svg width="24" height="24" viewBox="0 0 24 24"><path d="M6 2l4 5-2 3c1 3 3 5 6 6l3-2 5 4-2 4c-9 0-18-9-18-18z" fill="#fff"/></svg></span>
    <div><small>Call Us</small><strong>+1 555-010-4477</strong></div>
  </div>
  <div class="line"></div>
  <nav class="footer-nav"><a href="#">Home</a><a href="#">About</a><a href="#">Services</a><a href="#">News</a><a href="#contact">Contact</a></nav>
  <p class="copyright">2025 Quorvex Amber Frontier. All Rights Reserved.</p>
</footer>

</body>
</html>
```